Packaging for new retail dips "Quellmor"

* We require packaging for our new retail dip range.
* We have a small "Our Story" write up that we would like somewhere...
* We have approx. 7 different flavours - Hommous, Mediterranean Olive, Beetroot, Tzatziki etc. We would like one design where we can change the colour panel and the name of the dip.
* We are looking for a modern, clean, gourmet looking design - not the usual dip packaging you see on supermarket shelves.
* See my inspiration photo's.
* The Dieline attached is to scale.
Updates
Project Deadline Extended
Reason: Extension due to Dielines and Measurements not uploaded when we thought they were.
Target Market(s)
Will be going into retail supermarkets.
Industry/Entity Type
Retail
Font styles to use
Colors
Designer to choose colors to be used in the design.
Requirements
Must have
- * Please use our 'Quellmor' logo on the front and on the front side (if possible).
Nice to have
- * 'taste is everything' somewhere...
Should not have
- * No photo's of dips or photo's in general.

```html
<!DOCTYPE html>
<html lang="en">
<head>
<meta charset="utf-8">
<title>Quellmor Dip Range Packaging</title>
<link rel="stylesheet" href="https://fonts.googleapis.com/css2?family=Lato:wght@400;700&display=swap">
<style>
  :root {
    --canvas: #ffffff;
    --ink: #231f20;
    --band: #2a2627;
    --gold: #c9c27a;
    --gold-deep: #8f8a3c;
    --tub: #b8b579;
    --tub-light: #d8d6a4;
    --olive-top: #8c8a32;
    --olive-bottom: #6a6629;
    --beet-top: #b11a42;
    --beet-bottom: #8c1533;
    --label-text: #ffffff;
  }
  * { box-sizing: border-box; margin: 0; padding: 0; }
  html, body { width: 1200px; height: 830px; overflow: hidden; background: var(--canvas); }
  .canvas { position: relative; width: 1200px; height: 830px; }

  .tub {
    position: absolute;
    width: 492px; height: 492px;
    border-radius: 50%;
    background: radial-gradient(circle at 50% 50%, var(--tub-light) 0%, var(--tub) 70%, var(--gold-deep) 100%);
  }
  .tub--olive { left: 106px; top: 205px; }
  .tub--beet  { left: 632px; top: 205px; }

  .pack {
    position: absolute;
    top: 220px;
    width: 470px; height: 462px;
    background: #fff;
    border: 1px solid var(--gold);
  }
  .pack--olive { left: 117px; --panel-top: var(--olive-top); --panel-bottom: var(--olive-bottom); }
  .pack--beet  { left: 643px; --panel-top: var(--beet-top);  --panel-bottom: var(--beet-bottom); }

  .pack__lip {
    position: absolute; left: -1px; right: -1px; top: -8px; height: 8px;
    background: linear-gradient(90deg, var(--panel-bottom) 0 32%, var(--tub-light) 32% 68%, var(--panel-bottom) 68% 100%);
  }

  .brand {
    position: absolute; left: 0; width: 322px; top: 165px;
    text-align: center;
  }
  .brand__name {
    font-family: 'Lato', sans-serif;
    font-weight: 400;
    font-size: 40px;
    color: var(--ink);
    text-transform: uppercase;
    line-height: 1;
  }
  .brand__tagline {
    margin-top: 8px;
    font-family: 'Lato', sans-serif;
    font-weight: 400;
    font-size: 15px;
    color: var(--ink);
  }

  .pack__rule {
    position: absolute; left: 0; right: 0; height: 2px; background: var(--gold);
  }
  .pack__rule--upper { top: 269px; }
  .pack__rule--lower { top: 314px; }
  .pack__band {
    position: absolute; left: 0; right: 0; top: 274px; height: 37px;
    background: var(--band);
  }
  .pack__panel {
    position: absolute; left: 0; right: 0; top: 318px; bottom: 0;
    background: linear-gradient(180deg, var(--panel-top) 0%, var(--panel-top) 45%, var(--panel-bottom) 100%);
  }
  .pack__flavour {
    position: absolute; left: 32px; top: 24px;
    font-family: 'Lato', sans-serif;
    font-weight: 700;
    font-size: 28px;
    line-height: 1.18;
    color: var(--label-text);
  }
  .pack__weight {
    position: absolute; left: 357px; top: 92px;
    font-family: 'Lato', sans-serif;
    font-size: 15px;
    color: var(--label-text);
  }
  .seal {
    position: absolute; left: 309px; top: 232px;
    width: 118px; height: 118px;
  }
</style>
</head>
<body>
<main class="canvas">
  <div class="tub tub--olive"></div>
  <div class="tub tub--beet"></div>

  <section class="pack pack--olive">
    <div class="pack__lip"></div>
    <div class="brand">
      <p class="brand__name">Quellmor</p>
      <p class="brand__tagline">made close to home</p>
    </div>
    <div class="pack__rule pack__rule--upper"></div>
    <div class="pack__band"></div>
    <div class="pack__rule pack__rule--lower"></div>
    <div class="pack__panel">
      <h2 class="pack__flavour">Mediterranean<br>Olive</h2>
      <p class="pack__weight">200 g</p>
    </div>
    <svg class="seal" viewBox="0 0 118 118" role="img" aria-label="Round seal badge">
      <circle cx="59" cy="59" r="57" fill="var(--gold)"/>
      <circle cx="59" cy="59" r="53" fill="var(--band)"/>
      <circle cx="59" cy="59" r="38" fill="none" stroke="var(--gold)" stroke-width="2"/>
    </svg>
  </section>

  <section class="pack pack--beet">
    <div class="pack__lip"></div>
    <div class="brand">
      <p class="brand__name">Quellmor</p>
      <p class="brand__tagline">made close to home</p>
    </div>
    <div class="pack__rule pack__rule--upper"></div>
    <div class="pack__band"></div>
    <div class="pack__rule pack__rule--lower"></div>
    <div class="pack__panel">
      <h2 class="pack__flavour">Beetroot</h2>
      <p class="pack__weight">200 g</p>
    </div>
    <svg class="seal" viewBox="0 0 118 118" role="img" aria-label="Round seal badge">
      <circle cx="59" cy="59" r="57" fill="var(--gold)"/>
      <circle cx="59" cy="59" r="53" fill="var(--band)"/>
      <circle cx="59" cy="59" r="38" fill="none" stroke="var(--gold)" stroke-width="2"/>
    </svg>
  </section>
</main>
</body>
</html>
```